Minimalist Professional Business Card Design

We will be revamping our marketing materials: Business cards, Website and Catalogs.
Our Overall Design direction is to have a Minimalist artwork with Professionalism and Premium feel. The revamp starts with the new business card design followed by the others. Thus the designer whom work is selected for this job will likely to follow through with the subsequent jobs.

Target Market(s)

Upscale

Industry/Entity Type

Manufacturing

Contact Information for Business Card

For the Business Cards, the following are required:
. Minimalist yet Professional and Premium Feel
. Background Colors: white and / or light pastel yellow and if needed to smoothen the yellow, the light grey can be incorporated. We are changing our corporate bright yellow to either one of the three alternatives:
1. Soylant yellow CMYK (1%, 0%, 52%, 3%)
2. Popcorn yellow CMYK (0%, 0%, 33%, 0%)
3. Papaya yellow CMYK (0%, 0%, 51%, 0%)

Information to be inputed in the business cards:

Name: Barlen Moritova
Position: Managing Director

Company's name: Vellomar Valves Pte. Ltd.
Address: 512 Halvick Lane #07-09B
Singapore 617302
Tel: (65) 6281 4096
Fax: (65) 6294 7118
Email: barlen@vellomarvalves-example.com
Website: www.vellomarvalves-example.com
Skype: Vellomar.Valves
Whatsapp/ Line/ Viber/ WeChat: (65) 9372 6081

Company's Logo
Company's Slogan
Two product photos placed side by side (if this gets into the way of the design, it is OK not to include them)

Font styles to use
Serif

Colors
ffffff

Requirements
Must have
• Minimalist
Should not have
• Messy, crowded, playful

```html
<!DOCTYPE html>
<html lang="en">
<head>
<meta charset="utf-8">
<title>Vellomar Valves – Business Card</title>
<link href="https://fonts.googleapis.com/css2?family=Arimo:ital,wght@0,400;0,700;1,400;1,700&display=swap" rel="stylesheet">
<style>
  :root {
    --backdrop: #b5cad7;
    --card: #ffffff;
    --frame: #f2eba0;
    --ink: #2b2b2b;
    --ink-soft: #7a7a7a;
    --ink-mid: #555555;
    --icon: #333333;
  }
  * { box-sizing: border-box; margin: 0; padding: 0; }
  html, body {
    width: 1200px; height: 800px; overflow: hidden;
    background: var(--backdrop);
    font-family: "Arimo", Arial, sans-serif;
    color: var(--ink);
  }
  .stage {
    width: 1200px; height: 800px;
    display: flex; align-items: center; justify-content: center; gap: 40px;
  }
  .card {
    position: relative;
    width: 520px; height: 310px;
    background: var(--card);
    border-radius: 14px;
    box-shadow: 0 12px 30px rgba(60, 85, 100, 0.18);
  }
  .card__frame {
    position: absolute; inset: 22px;
    border: 1.5px solid var(--frame);
    border-radius: 26px;
  }
  /* Front face */
  .card--front .brand-block {
    position: absolute; inset: 0;
    display: flex; flex-direction: column; align-items: center; justify-content: center;
  }
  .brand-mark {
    display: flex; align-items: center; gap: 8px;
    font-weight: 700; font-size: 20px; letter-spacing: 1px; color: var(--ink-soft);
  }
  .brand-mark__dot {
    width: 26px; height: 26px; border-radius: 50%;
    border: 2px solid var(--ink-soft);
  }
  .company-name { margin-top: 12px; font-size: 15px; color: var(--ink-soft); }
  .slogan { margin-top: 6px; font-size: 15px; font-style: italic; font-weight: 700; color: var(--ink-soft); }
  /* Info face */
  .card--info .brand-corner {
    position: absolute; left: 50px; top: 40px;
  }
  .card--info .brand-corner .brand-mark { font-size: 16px; }
  .card--info .brand-corner .brand-mark__dot { width: 20px; height: 20px; }
  .card--info .brand-corner .company-name { margin-top: 6px; font-size: 12px; }
  .contact-list { list-style: none; }
  .contact-list li {
    display: flex; align-items: flex-start; gap: 8px;
    font-size: 11px; font-weight: 700; line-height: 1.35; color: var(--ink-mid);
    margin-bottom: 6px;
  }
  .contact-list svg { flex: none; width: 14px; height: 14px; fill: var(--icon); }
  .contacts-left { position: absolute; left: 50px; top: 112px; }
  .messengers {
    position: absolute; left: 50px; bottom: 48px;
    display: flex; align-items: center; gap: 8px;
    font-size: 11px; font-weight: 700; color: var(--ink-mid);
  }
  .messengers__icon { width: 15px; height: 15px; border-radius: 50%; background: var(--icon); }
  .messengers__number { margin-left: 8px; }
  .person { position: absolute; right: 50px; top: 96px; text-align: right; }
  .person__name { font-size: 24px; font-weight: 700; color: var(--ink); }
  .person__title { font-size: 12px; font-weight: 700; color: var(--ink-mid); margin-top: 2px; }
  .contacts-right { position: absolute; right: 50px; top: 168px; }
  .contacts-right li { justify-content: flex-end; }
  .plain-circle { flex: none; width: 14px; height: 14px; border-radius: 50%; border: 2px solid var(--icon); }
</style>
</head>
<body>
<main class="stage">
  <section class="card card--front" aria-label="Card front">
    <div class="card__frame"></div>
    <div class="brand-block">
      <div class="brand-mark"><span class="brand-mark__dot"></span>VELLOMAR</div>
      <p class="company-name">Vellomar Valves Pte. Ltd.</p>
      <p class="slogan">Built With Care I For Lasting Flow</p>
    </div>
  </section>

  <section class="card card--info" aria-label="Card back">
    <div class="card__frame"></div>
    <div class="brand-corner">
      <div class="brand-mark"><span class="brand-mark__dot"></span>VELLOMAR</div>
      <p class="company-name">Vellomar Valves Pte. Ltd.</p>
    </div>

    <ul class="contact-list contacts-left">
      <li><svg viewBox="0 0 24 24"><path d="M6.6 10.8a15 15 0 0 0 6.6 6.6l2.2-2.2c.3-.3.7-.4 1-.2 1.1.4 2.3.6 3.6.6.6 0 1 .4 1 1V20c0 .6-.4 1-1 1A17 17 0 0 1 3 4c0-.6.4-1 1-1h3.5c.6 0 1 .4 1 1 0 1.3.2 2.5.6 3.6.1.3 0 .7-.2 1z"/></svg>(65) 6281 4096</li>
      <li><svg viewBox="0 0 24 24"><path d="M12 2a7 7 0 0 0-7 7c0 5.2 7 13 7 13s7-7.8 7-13a7 7 0 0 0-7-7zm0 9.5A2.5 2.5 0 1 1 12 6.5a2.5 2.5 0 0 1 0 5z"/></svg><span>512 Halvick Lane #07-09B<br>Singapore 617302</span></li>
      <li><svg viewBox="0 0 24 24"><path d="M6 2h10l2 2v5H6zM3 10h18a1 1 0 0 1 1 1v7h-4v4H6v-4H2v-7a1 1 0 0 1 1-1zm5 6v4h8v-4z"/></svg>(65) 6294 7118</li>
    </ul>

    <div class="messengers">
      <span class="messengers__icon"></span>
      <span class="messengers__icon"></span>
      <span class="messengers__icon"></span>
      <span class="messengers__icon"></span>
      <span class="messengers__number">(65) 9372 6081</span>
    </div>

    <div class="person">
      <h1 class="person__name">Barlen Moritova</h1>
      <p class="person__title">Managing Director</p>
    </div>

    <ul class="contact-list contacts-right">
      <li>barlen@vellomarvalves-example.com<svg viewBox="0 0 24 24"><path d="M2 5h20v14H2zm2 2v.5l8 5 8-5V7zm0 3v7h16v-7l-8 5z"/></svg></li>
      <li>www.vellomarvalves-example.com<svg viewBox="0 0 24 24"><path d="M12 2a10 10 0 1 0 0 20 10 10 0 0 0 0-20zm6.9 9h-3a15 15 0 0 0-1.3-6A8 8 0 0 1 18.9 11zM12 4c.9 1.3 1.7 3.9 1.9 7h-3.8c.2-3.1 1-5.7 1.9-7zM9.4 5a15 15 0 0 0-1.3 6h-3A8 8 0 0 1 9.4 5zM5.1 13h3a15 15 0 0 0 1.3 6 8 8 0 0 1-4.3-6zm6.9 7c-.9-1.3-1.7-3.9-1.9-7h3.8c-.2 3.1-1 5.7-1.9 7zm2.6-1a15 15 0 0 0 1.3-6h3a8 8 0 0 1-4.3 6z"/></svg></li>
      <li>Vellomar.Valves<span class="plain-circle"></span></li>
    </ul>
  </section>
</main>
</body>
</html>
```